Larkmoor Health- Core Values Graphic for Visual Appeal

I would like a poster that could take these written core values from our organization and create a graphic that we could use for our staff and employees. I would also like to incorporate our branding into this project. Thank you!

Target Market(s)

To helps patients and employees understand the core values of our organization

Industry/Entity Type

Healthcare

Requirements
Must have
• Match our branding
Nice to have
• Please use your creativity!
Should not have
• Overly complex/ busy

```html
<!DOCTYPE html>
<html lang="en">
<head>
<meta charset="utf-8">
<title>Larkmoor Health – Core Values</title>
<link rel="stylesheet" href="https://fonts.googleapis.com/css2?family=Archivo+Black&family=Open+Sans:wght@400;700&display=swap">
<style>
  :root {
    --blue: #2a9fd8;
    --ink: #2d2d2d;
    --line-blue: #8cc4e4;
    --line-grey: #8a8f94;
    --paper: #f3f5f6;
    --tint: #cfe6f3;
    --icon-fill: #d9ebf5;
    --white: #ffffff;
  }
  html, body { margin: 0; padding: 0; overflow: hidden; }
  body { width: 925px; height: 1200px; }
  .poster {
    position: relative;
    width: 925px;
    height: 1200px;
    overflow: hidden;
    background: linear-gradient(135deg, var(--tint) 0%, var(--paper) 30%, var(--paper) 65%, var(--tint) 100%);
    font-family: "Open Sans", Arial, sans-serif;
  }
  .artwork { position: absolute; inset: 0; }
  .value-word { font-family: "Archivo Black", "Arial Black", sans-serif; font-size: 134px; }
  .value-word.blue { fill: var(--blue); }
  .value-word.dark { fill: var(--ink); }
  .connector { fill: none; stroke-width: 2.5; stroke-linejoin: round; opacity: .8; }
  .connector.blue { stroke: var(--line-blue); }
  .connector.grey { stroke: var(--line-grey); }
  .icon-slot { fill: var(--icon-fill); }

  .headline {
    position: absolute;
    right: 56px;
    top: 44px;
    margin: 0;
    font-family: "Archivo Black", "Arial Black", sans-serif;
    font-size: 73px;
    line-height: 63px;
    text-align: right;
    color: var(--blue);
    font-weight: 400;
  }
  .value-text {
    position: absolute;
    left: 626px;
    width: 256px;
    margin: 0;
    font-size: 10.6px;
    line-height: 14.2px;
    text-align: justify;
  }
  .value-text.blue { color: var(--blue); }
  .value-text.dark { color: var(--ink); }
  .value-family { top: 247px; }
  .value-excellence { top: 388px; }
  .value-integrity { top: 543px; }
  .value-service { top: 698px; }

  .web-tab {
    position: absolute;
    left: 0;
    top: 933px;
    width: 46px;
    height: 255px;
    background: var(--ink);
    border-radius: 0 22px 0 0;
  }
  .web-tab span {
    position: absolute;
    left: 50%;
    top: 50%;
    transform: translate(-50%, -50%) rotate(-90deg);
    color: var(--white);
    font-size: 17px;
    letter-spacing: .5px;
    white-space: nowrap;
  }
  .brand {
    position: absolute;
    left: 650px;
    top: 1040px;
    width: 210px;
    text-align: center;
  }
  .brand-dot {
    display: block;
    width: 26px;
    height: 26px;
    margin: 0 auto 10px;
    border-radius: 50%;
    background: var(--blue);
  }
  .brand-name {
    font-weight: 700;
    font-size: 30px;
    color: var(--ink);
    letter-spacing: .5px;
  }
</style>
</head>
<body>
<main class="poster">
  <svg class="artwork" width="925" height="1200" viewBox="0 0 925 1200" aria-hidden="false">
    <path class="connector blue" d="M118 274 V98 Q118 90 126 90 H455 Q463 90 463 98 V243 Q463 251 471 251 H626"/>
    <path class="connector grey" d="M295 170 H504 Q512 170 512 178 V382 Q512 390 520 390 H626"/>
    <path class="connector blue" d="M455 960 V438 Q455 430 463 430 H560 Q568 430 568 438 V545 H626"/>
    <path class="connector grey" d="M590 1120 V700 H626"/>

    <text class="value-word blue" transform="translate(164 762) rotate(-90)" textLength="485" lengthAdjust="spacingAndGlyphs">FAMILY</text>
    <text class="value-word dark" transform="translate(295 1021) rotate(-90)" textLength="882" lengthAdjust="spacingAndGlyphs">EXCELENCE</text>
    <text class="value-word blue" transform="translate(435 967) rotate(-90)" textLength="685" lengthAdjust="spacingAndGlyphs">INTIGRITY</text>
    <text class="value-word dark" transform="translate(582 1147) rotate(-90)" textLength="587" lengthAdjust="spacingAndGlyphs">SERVICE</text>

    <rect class="icon-slot" x="53" y="788" width="126" height="99" rx="10" role="img" aria-label="Line icon of a family group"/>
    <rect class="icon-slot" x="478" y="443" width="106" height="99" rx="10" role="img" aria-label="Line icon of hands holding a gear"/>
    <rect class="icon-slot" x="343" y="990" width="101" height="90" rx="10" role="img" aria-label="Line icon of a shield above a handshake"/>
    <rect class="icon-slot" x="198" y="1044" width="101" height="107" rx="10" role="img" aria-label="Blue award ribbon badge icon"/>
  </svg>

  <h1 class="headline">CORE<br>VALUES</h1>

  <p class="value-text blue value-family">Family: At the heart of our mission is the commitment to provide high-quality, affordable healthcare in a comforting and uplifting family-oriented environment. Just as our community is our extended family, every patient is cherished member of our healthcare family. We treat each individual with the same care, compassion, and respect we would offer to our own loved ones.</p>

  <p class="value-text dark value-excellence">Excellence: In line with our goal, we aspire not only to alleviate pain but also to inspire patients to become active participants in their well-being. We believe in empowering our patients through education and compassion. Our pursuit of excellence is unwavering, driven by our dedication to continuously improve our services at every level, ensuring that our community receives nothing less than exceptional care.</p>

  <p class="value-text blue value-integrity">Integrity: In our healthcare team, 'Integrity' is non-negotiable. Our purpose is deeply rooted in ethics, integrity, and professional standards. We operate with the utmost integrity in every aspect of our work, adhering to the highest ethical principles. We understand that trust is the foundation of healthcare, and we are committed to maintaining the trust our community places in us.</p>

  <p class="value-text dark value-service">Service: Our vision is grounded in the belief that every person possesses the innate potential for true health. We aim to facilitate the body's natural healing response by providing the highest level of service. Our hope for each patient extends beyond healing; we aspire to help you fulfill your life's mission and purpose abundantly, supporting you in your journey to well-being.</p>

  <div class="web-tab"><span>WWW.WEBSITE.COM</span></div>

  <div class="brand">
    <span class="brand-dot"></span>
    <span class="brand-name">Larkmoor Health</span>
  </div>
</main>
</body>
</html>
```